Super elegant, crisp & clean Business card design required

We recently upgraded our branding - which is on our website - tavorelstudio.com

I would like a simple, yet elegant, clean business card design please.

The font of my logo is Cinzel - and because of the natural colour - it's best to have this on a black background.

I would like to have the back of the business card - with simply my logo.

PLEASE DO NOT SUBMIT A COMPLICATED / UNCLEAN DESIGN

Industry/Entity Type

Business

Contact Information for Business Card

Dalvik Ostrander Photography

Font styles to use
Other font styles liked:
• Cinzel

Requirements
Must have
• A backpage with nothing but my logo
• Simple design - stands out
Should not have
• Colour that dont align with my logo
• Over complicated '/ non symmetrical design

```html
<!DOCTYPE html>
<html lang="en">
<head>
<meta charset="utf-8">
<title>Dalvik Ostrander Photography – Business Card</title>
<link rel="stylesheet" href="https://fonts.googleapis.com/css2?family=Cinzel:wght@400&display=swap">
<style>
  :root {
    --backdrop: #ffffff;
    --card: #1b1b1b;
    --gold: #857459;
    --shadow: rgba(0, 0, 0, 0.28);
  }
  * { box-sizing: border-box; margin: 0; padding: 0; }
  html, body {
    width: 1200px;
    height: 1000px;
    overflow: hidden;
    background: var(--backdrop);
  }
  .canvas {
    position: relative;
    width: 1200px;
    height: 1000px;
    font-family: "Cinzel", "Times New Roman", serif;
    color: var(--gold);
  }
  .card {
    position: absolute;
    left: 220px;
    width: 760px;
    height: 430px;
    background: var(--card);
    box-shadow: 0 4px 10px var(--shadow);
  }
  .card--front { top: 50px; }
  .card--back  { top: 520px; }

  /* Front: name set in place of the mark */
  .brand {
    position: absolute;
    inset: 0;
    display: flex;
    flex-direction: column;
    align-items: center;
    justify-content: center;
    gap: 18px;
  }
  .brand__dot {
    width: 64px;
    height: 64px;
    border-radius: 50%;
    border: 2px solid var(--gold);
  }
  .brand__name {
    font-size: 34px;
    font-weight: 400;
    letter-spacing: 1px;
    line-height: 1.1;
    text-align: center;
  }
  .brand__name span { display: block; font-size: 15px; letter-spacing: 14px; margin-top: 8px; padding-left: 14px; }

  /* Back: contact details */
  .contact__title {
    position: absolute;
    left: 110px;
    top: 140px;
    font-size: 19px;
    letter-spacing: 1.5px;
  }
  .contact__list {
    position: absolute;
    left: 120px;
    top: 232px;
    display: grid;
    grid-template-columns: 150px 1px auto;
    column-gap: 26px;
    font-size: 15px;
    letter-spacing: 0.8px;
    line-height: 20px;
  }
  .contact__labels, .contact__values { display: flex; flex-direction: column; }
  .contact__labels { padding-top: 30px; }
  .contact__rule { background: var(--gold); height: 58px; margin-top: 14px; }
  .contact__values { padding-top: 0; }
</style>
</head>
<body>
<main class="canvas">
  <section class="card card--front" aria-label="Card front">
    <div class="brand">
      <div class="brand__dot"></div>
      <p class="brand__name">Dalvik Ostrander<span>Photography</span></p>
    </div>
  </section>

  <section class="card card--back" aria-label="Card back">
    <h1 class="contact__title">Dalvik Ostrander Photography</h1>
    <div class="contact__list">
      <div class="contact__labels">
        <span>Phone</span>
        <span>Website</span>
        <span>Email Address</span>
      </div>
      <div class="contact__rule"></div>
      <div class="contact__values">
        <span>07700900418</span>
        <span>tavorelstudio.com</span>
        <span>do.photography@tavorelmail.com</span>
      </div>
    </div>
  </section>
</main>
</body>
</html>
```